small auto electrical company needs new logo and business cards !!!

we are a small auto electrical company (Velmor Autos Ltd) that has been running for 13 years the logo we have was put together by dinosaurs so we are looking at re branding the company starting with business cards and a new logo we fit GPS tracking devices for young drivers through there insurance company also we fit hands free systems and dash cameras also safety locks to fleet vehicles we would like bright eye catching colours day glow and neon and quirky designs for the logo our original logo was baby blue which i have added a picture enclosed we would like double sided but have a space to write notes and prices preferably not white on back same colour throughout many thanks
Reason: Just a chance to finalise any designs we want VA logos or V logos - No vlm's and no dinosaurs lol
Business
Installs@velmorautos.co.uk
07922483617
www.Velmorautos.co.uk
Velmor Autos Ltd - Fleets and Insurance Services
- new logo design !!
- Satellite in logo or something attaining to gps
- maybe a car in the logo
- shouldnt have velmor as vlm it is VeLMOR Autos

```html
<!DOCTYPE html>
<html lang="en">
<head>
<meta charset="utf-8">
<title>Velmor Autos Ltd – Business Card</title>
<link rel="stylesheet" href="https://fonts.googleapis.com/css2?family=Marcellus&family=Questrial&family=Lato:wght@400&family=Crimson+Text:wght@400;700&display=swap">
<style>
  :root {
    --backdrop: #000000;
    --card-light: #e6f6fd;
    --brand-blue: #0a8fd6;
    --ink-blue: #0779b8;
    --neon: #c8ff1a;
    --ink-grey: #4f5a62;
    --ink-dark: #2e3338;
    --white: #ffffff;
  }
  html, body {
    margin: 0;
    padding: 0;
    width: 1200px;
    height: 900px;
    overflow: hidden;
    background: var(--backdrop);
  }
  .canvas {
    position: relative;
    width: 1200px;
    height: 900px;
    background: var(--backdrop);
  }
  .card {
    position: absolute;
    top: 200px;
    width: 310px;
    height: 502px;
    box-sizing: border-box;
  }
  .card--front {
    left: 293px;
    background: var(--card-light);
    border-radius: 55px 0 65px 0;
  }
  .card--back {
    left: 613px;
    width: 308px;
    background: var(--brand-blue);
    border-radius: 0 55px 0 65px;
  }
  .brand {
    position: absolute;
    left: 0;
    width: 100%;
    text-align: center;
  }
  .brand__dot {
    display: block;
    margin: 0 auto;
    border-radius: 50%;
  }
  .brand__name {
    display: block;
    font-family: "Marcellus", serif;
    font-size: 25px;
    line-height: 1;
    letter-spacing: -0.6px;
    white-space: nowrap;
  }
  .brand__tagline {
    display: block;
    font-family: "Questrial", sans-serif;
    font-size: 16px;
    line-height: 1;
    margin-top: 4px;
    white-space: nowrap;
  }
  .card--front .brand { top: 44px; left: 16px; }
  .card--front .brand__dot { width: 58px; height: 58px; background: var(--ink-blue); margin-bottom: 23px; }
  .card--front .brand__name { color: var(--ink-blue); }
  .card--front .brand__tagline { color: var(--ink-grey); }

  .card--back .brand { top: 186px; left: 1px; }
  .card--back .brand__dot { width: 62px; height: 62px; background: var(--white); margin-bottom: 24px; }
  .card--back .brand__name { color: var(--white); }
  .card--back .brand__tagline { color: var(--neon); }

  .person {
    position: absolute;
    left: 30px;
    top: 293px;
  }
  .person__name {
    margin: 0;
    font-family: "Crimson Text", serif;
    font-weight: 700;
    font-size: 22px;
    line-height: 1;
    color: var(--ink-blue);
  }
  .person__role {
    margin: 3px 0 0;
    font-family: "Crimson Text", serif;
    font-size: 14px;
    line-height: 1;
    color: var(--ink-grey);
  }
  .contact {
    position: absolute;
    left: 30px;
    top: 352px;
    margin: 0;
    padding: 0;
    list-style: none;
    font-family: "Lato", sans-serif;
    font-size: 14px;
    color: var(--ink-dark);
  }
  .contact__item {
    display: flex;
    align-items: center;
    height: 18px;
  }
  .contact__icon {
    width: 10px;
    height: 10px;
    margin-right: 9px;
    fill: var(--ink-blue);
  }
  .address {
    position: absolute;
    left: 30px;
    top: 421px;
    margin: 0;
    font-style: normal;
    font-family: "Lato", sans-serif;
    font-size: 14px;
    line-height: 18px;
    color: var(--ink-dark);
  }
  .notes {
    position: absolute;
    left: 34px;
    right: 34px;
    top: 352px;
  }
  .notes__label {
    margin: 0 0 6px;
    font-family: "Questrial", sans-serif;
    font-size: 12px;
    letter-spacing: 1px;
    color: var(--neon);
  }
  .notes__line {
    height: 26px;
    border-bottom: 1px solid rgba(255, 255, 255, 0.55);
  }
</style>
</head>
<body>
<main class="canvas">
  <section class="card card--front" aria-label="Business card front">
    <div class="brand">
      <span class="brand__dot"></span>
      <span class="brand__name">VELMOR AUTOS LTD</span>
      <span class="brand__tagline">Fleet &amp; Insurance Services</span>
    </div>

    <div class="person">
      <p class="person__name">ALAN BROOKS</p>
      <p class="person__role">PRESIDENT</p>
    </div>

    <ul class="contact">
      <li class="contact__item">
        <svg class="contact__icon" viewBox="0 0 10 10" aria-hidden="true"><path d="M1 3.5C1 2 3 1.5 5 1.5S9 2 9 3.5V4.5H7V3.5H3V4.5H1Z M2.5 5L3.5 4H6.5L7.5 5V8.5H2.5Z"/></svg>
        (514)555-0193
      </li>
      <li class="contact__item">
        <svg class="contact__icon" viewBox="0 0 10 10" aria-hidden="true"><path d="M1 2.5H9V8H1Z"/><path d="M1.5 3L5 5.6L8.5 3" stroke="var(--card-light)" stroke-width="0.8" fill="none"/></svg>
        info@velmorautos.com
      </li>
      <li class="contact__item">
        <svg class="contact__icon" viewBox="0 0 10 10" aria-hidden="true"><circle cx="5" cy="5" r="4.5"/><path d="M3 3.5L5 3L6 4.5L4.5 6L5 8L3.5 7Z" fill="var(--card-light)"/></svg>
        www.velmorautos.com
      </li>
    </ul>

    <address class="address">
      4470 Rue Belmont<br>
      Montreal, QC<br>
      H2T1K9
    </address>
  </section>

  <section class="card card--back" aria-label="Business card back">
    <div class="brand">
      <span class="brand__dot"></span>
      <span class="brand__name">VELMOR AUTOS LTD</span>
      <span class="brand__tagline">Fleet &amp; Insurance Services</span>
    </div>

    <div class="notes" aria-label="Space for notes and prices">
      <p class="notes__label">NOTES &amp; PRICES</p>
      <div class="notes__line"></div>
      <div class="notes__line"></div>
      <div class="notes__line"></div>
      <div class="notes__line"></div>
    </div>
  </section>
</main>
</body>
</html>
```